Redesign our business cards for PRD, We had some business cards designed but we dont like the style and dont think they are professional enough please can you redesign them thanks

```html
<!DOCTYPE html>
<html lang="en">
<head>
<meta charset="utf-8">
<title>PRD Business Cards</title>
<link rel="stylesheet" href="https://fonts.googleapis.com/css2?family=Montserrat:wght@400;500;600;700&display=swap">
<style>
  :root {
    --backdrop: #f1f1f1;
    --ink: #111111;
    --paper: #ffffff;
    --night: #000000;
    --muted: #3a3a3a;
  }
  * { margin: 0; padding: 0; box-sizing: border-box; }
  html, body {
    width: 1200px;
    height: 907px;
    overflow: hidden;
    background: var(--backdrop);
    font-family: "Montserrat", Arial, sans-serif;
  }
  .canvas { position: relative; width: 1200px; height: 907px; }

  .card {
    position: absolute;
    width: 640px;
    height: 355px;
    box-shadow: 0 6px 18px rgba(0,0,0,0.12);
  }
  .card--foundation { left: 110px; top: 70px; background: var(--paper); color: var(--ink); }
  .card--studio { left: 450px; top: 480px; background: var(--night); color: var(--paper); }

  .wordmark {
    position: absolute;
    top: 30px;
    right: 34px;
    text-align: right;
    font-weight: 600;
    line-height: 1;
  }
  .wordmark__name { display: block; font-size: 56px; letter-spacing: 1px; }
  .wordmark__line { display: block; font-size: 21px; letter-spacing: 5px; margin-top: 6px; }
  .wordmark__tagline { display: block; font-size: 10px; font-weight: 400; letter-spacing: 0.3px; margin-top: 5px; }

  .holder {
    position: absolute;
    left: 30px;
    top: 170px;
    font-size: 21px;
    font-weight: 400;
    letter-spacing: 0.5px;
  }
  .holder strong { font-weight: 700; }
  .holder__role { display: block; font-size: 12px; font-weight: 500; margin-top: 18px; letter-spacing: 0.3px; }

  .contact {
    position: absolute;
    bottom: 28px;
    font-size: 13px;
    font-weight: 500;
    line-height: 21px;
    list-style: none;
  }
  .contact--left { left: 30px; }
  .contact--right { right: 30px; text-align: right; }

  .card--foundation .holder { top: 148px; }
  .card--foundation .contact { color: var(--muted); }
</style>
</head>
<body>
  <main class="canvas">
    <section class="card card--foundation" aria-label="PRD Foundation business card">
      <div class="wordmark">
        <span class="wordmark__name">PRD</span>
        <span class="wordmark__line">FOUNDATION</span>
        <span class="wordmark__tagline">Steady Steps Bold Work</span>
      </div>
      <div class="holder">
        <strong>MARLO</strong> HENDRY
        <span class="holder__role">Founder</span>
      </div>
      <ul class="contact contact--left">
        <li>+44 7700 900 318</li>
        <li>prdfoundation.com</li>
        <li>marlo@prdfoundation.com</li>
      </ul>
    </section>

    <section class="card card--studio" aria-label="PRD Studio business card">
      <div class="wordmark">
        <span class="wordmark__name">PRD</span>
        <span class="wordmark__line">STUDIO</span>
        <span class="wordmark__tagline">Create and Deliver</span>
      </div>
      <div class="holder">
        <strong>MARLO</strong> HENDRY
      </div>
      <ul class="contact contact--left">
        <li>+44 7700 900 318</li>
        <li>prdstudio.com</li>
        <li>marlo@prdstudio.com</li>
      </ul>
      <ul class="contact contact--right">
        <li>chirpline.net/prdstudio</li>
        <li>friendwall.net/prdstudio</li>
        <li>snapgrid.net/prdstudio</li>
      </ul>
    </section>
  </main>
</body>
</html>
```